Web Design Project

We are looking for a beautiful, clean web page design for our new web service: Tavernik. The idea behind tavernik is simple. People tell us where they live and what they love, and we point them towards interesting offers, places and events near them - as reviewed by our experts and their friends. It is available on the web and by phone. We have chosen our logo and know the elements we want on each page. Now we just need a whole a great design to pull it all together.
///
TaVernik
locate, explore and discover the best of your city with tavernik
Discover your cities hottest offers
places & venues while sharing
the things that mean the most to you.
Join for free today!
//
Note: we have also had some feedback that the name is difficult to read/pronounce, so we might want to change the color of the word be in tavernik so that it stands out. suggestions welcome.
Target Market(s)
Young, urban, savvy consumers
We are looking at this site for inspiration
https://strovento.example/
elements: blog:latest news, top picks // members area // categories: fashion & beauty; food & drink; entertainment & events

```html
<!DOCTYPE html>
<html lang="en">
<head>
<meta charset="utf-8">
<title>Tavernik</title>
<link href="https://fonts.googleapis.com/css2?family=Marcellus&family=Ubuntu:wght@400;500;700&family=Pinyon+Script&display=swap" rel="stylesheet">
<style>
:root{
  --page:#e2e2e2;
  --band:#c9c5c5;
  --hero:#ece8e8;
  --content:#f8efeb;
  --orange:#f25a1c;
  --orange-light:#fb8a1e;
  --orange-text:#f2620f;
  --ink:#3c3c3c;
  --text:#2e2e2e;
  --olive:#9a8a00;
  --script:#d9232a;
  --footer:#6b6b6b;
  --footer-text:#e6e6e6;
  --white:#fff;
}
*{box-sizing:border-box;margin:0;padding:0}
html,body{width:1011px;height:1200px;overflow:hidden}
body{background:var(--page);font-family:"Ubuntu",sans-serif;color:var(--text);position:relative}
h1,h2{font-weight:400}
.abs{position:absolute}
.hero-band{left:0;top:101px;width:1011px;height:351px;background:var(--band)}
.header{left:139px;top:0;width:759px;height:101px;background:linear-gradient(var(--orange-light),var(--orange))}
.nav{top:37px;left:0;width:1011px;font-size:11px;color:var(--white)}
.nav span{position:absolute;top:0}
.hero{left:139px;top:101px;width:759px;height:351px;background:radial-gradient(circle at 72% 40%,#f7d6dc 0,var(--hero) 45%)}
.ribbon{left:166px;top:0;width:172px;height:183px}
.logo-name{left:166px;top:95px;width:172px;text-align:center;font-size:27px;color:var(--white)}
.headline{left:164px;top:206px;width:370px;font-family:"Marcellus",serif;font-size:40px;line-height:52px;color:var(--ink);white-space:nowrap}
.subline{left:164px;top:305px;font-size:17px;color:var(--ink)}
.intro{left:171px;top:353px;font-size:9.6px;line-height:12px;font-weight:500}
.intro em{font-style:normal;color:var(--orange-text)}
.signup{left:168px;top:394px;width:160px;height:44px;background:linear-gradient(var(--orange-light),var(--orange));border:2px solid #fff;box-shadow:0 1px 3px rgba(0,0,0,.35);color:#fff;font-weight:700;font-size:23px;text-align:center;line-height:40px;letter-spacing:.5px}
.hero-photo{left:545px;top:164px;width:328px;height:224px;background:#fff;transform:rotate(-1deg);box-shadow:0 2px 6px rgba(0,0,0,.3)}
.hero-photo div{position:absolute;left:5px;top:5px;right:5px;bottom:5px;background:linear-gradient(#e9a23d,#d88a2c 45%,#8b6a4a 70%,#5c4632)}
.content{left:139px;top:452px;width:759px;height:593px;background:var(--content)}
.cat-title{left:168px;top:476px;font-size:18.5px;color:#222}
.cat-desc{left:168px;top:510px;font-size:9.3px;line-height:13px}
.cat-desc em{font-style:normal;color:var(--orange-text);font-size:11px;font-weight:500}
.card{left:167px;width:467px;height:107px;background:linear-gradient(90deg,#cfcfcf,#f4f4f4 50%,#fff);box-shadow:0 1px 2px rgba(0,0,0,.15)}
.card-label{position:absolute;left:17px;top:12px;width:166px;height:84px;border-left:2px solid #b9b9b9;border-bottom:2px solid #b9b9b9;padding:8px 0 0 10px;font-family:"Pinyon Script",cursive;font-size:25px;line-height:29px;color:var(--script)}
.card-photo{left:427px;width:181px;background:#fff;border:1px solid #b9a400}
.sidebar{left:635px;top:435px;width:241px;height:627px;background:#fff;box-shadow:0 0 4px rgba(0,0,0,.3)}
.side-bar{left:644px;width:224px;height:31px;background:linear-gradient(#f2f2f2,#c9c9c9);font-size:12px;color:#333;line-height:31px;padding-left:60px;letter-spacing:.5px}
.side-icon{left:656px;width:36px;height:36px}
.news{left:659px;width:200px}
.date{position:absolute;left:0;top:0;width:38px;height:50px;background:var(--orange);border:1px solid #c33;outline:1px solid #fff;outline-offset:-3px;color:#fff;text-align:center;font-size:22px;line-height:25px}
.date small{display:block;font-size:14px;line-height:18px;border-top:1px solid #fff;margin:0 3px}
.news-body{position:absolute;left:48px;top:0;width:150px}
.news-title{font-size:9px;font-weight:700;color:var(--orange-text);line-height:11.5px;letter-spacing:.3px}
.news-meta{font-size:8px;color:var(--olive);font-variant:small-caps;margin-top:7px}
.news-text{font-size:9px;line-height:11.2px;margin-top:9px;padding-left:2px}
.news-more{font-size:8px;font-style:italic;color:var(--olive);padding-left:2px}
.rule{left:648px;width:210px;height:1px;background:linear-gradient(90deg,transparent,#bbb,transparent)}
.picks-intro{left:662px;top:836px;font-size:8.6px;line-height:14px}
.thumb{width:84px;border:1px solid #ddd;padding:2px;background:#fff}
.thumb div{width:100%;height:100%}
.footer{left:139px;top:1045px;width:759px;height:155px;background:linear-gradient(#7a7a7a,var(--footer))}
.foot-logo{left:198px;top:1120px;font-size:21px;color:#bdbdbd}
.foot-mark{left:236px;top:1078px;width:26px;height:26px;background:#8d8d8d}
.copyright{left:163px;top:1152px;font-size:8.6px;color:var(--footer-text)}
.foot-links{right:152px;font-size:8.4px;color:var(--footer-text);text-align:right}
.foot-links i{font-style:normal;margin:0 8px}
</style>
</head>
<body>
<div class="abs hero-band"></div>
<div class="abs header"></div>
<nav class="abs nav">
  <span style="left:414px">Home</span>
  <span style="left:487px">About Us</span>
  <span style="left:575px">Categories</span>
  <span style="left:669px">Top Picks</span>
  <span style="left:756px">Blog</span>
  <span style="left:821px">Contact Us</span>
</nav>
<section class="abs hero"></section>
<svg class="abs ribbon" viewBox="0 0 172 183" aria-hidden="true">
  <defs><linearGradient id="rib" x1="0" y1="0" x2="0" y2="1"><stop offset="0" stop-color="#fb8a1e"/><stop offset="1" stop-color="#f0501a"/></linearGradient></defs>
  <path d="M0 0H172V181L86 152L0 181Z" fill="url(#rib)" stroke="#fff" stroke-width="1.5"/>
  <rect x="71" y="38" width="30" height="30" fill="#fff" opacity=".9"/>
</svg>
<div class="abs logo-name">tavernik</div>
<h1 class="abs headline">LOCATE, EXPLORE<br>AND DISCOVER</h1>
<p class="abs subline">The Best Of Your City With Tavernik</p>
<p class="abs intro">Discover your cities <em>hottest offers places &amp; venues</em> while sharing<br>the things that mean the most to you. <em>Join for free today!</em></p>
<div class="abs signup">SIGN UP</div>
<div class="abs hero-photo"><div role="img" aria-label="Photo of a person on a bench looking at a city skyline at golden sunset"></div></div>

<section class="abs content"></section>
<h2 class="abs cat-title">Categories</h2>
<p class="abs cat-desc">Click on a category of your interest and find related places, venues and events in your area.<br>Not a memeber yet? <em>Sign Up</em> here.</p>

<div class="abs card" style="top:564px"><div class="card-label">Fashion and<br>Beauty</div></div>
<div class="abs card-photo" style="top:560px;height:118px" role="img" aria-label="Photo of gold high-heeled shoes with pearl necklaces"><div style="margin:4px;height:108px;background:linear-gradient(135deg,#f6f1e6,#c9a35a 50%,#f3ede2)"></div></div>
<div class="abs card" style="top:710px"><div class="card-label">Food and<br>Drink</div></div>
<div class="abs card-photo" style="top:708px;height:111px" role="img" aria-label="Photo of a cola with ice and a hot dog on lettuce"><div style="margin:4px;height:101px;background:linear-gradient(90deg,#3a1a12,#7a4a2a 35%,#8cb43c 60%,#d86a2a)"></div></div>
<div class="abs card" style="top:858px"><div class="card-label">Entertainment<br>And Events</div></div>
<div class="abs card-photo" style="top:856px;height:111px" role="img" aria-label="Photo of event invitation cards with orange roses"><div style="margin:4px;height:101px;background:linear-gradient(90deg,#f0a030,#f3dc8c 40%,#f8f1dc)"></div></div>

<aside class="abs sidebar"></aside>
<div class="abs side-bar" style="top:442px">LATEST NEWS</div>
<svg class="abs side-icon" style="top:430px" viewBox="0 0 36 36" aria-hidden="true"><rect x="4" y="6" width="24" height="28" fill="#fff" stroke="#bbb" transform="rotate(-12 16 20)"/><path d="M30 4L17 24" stroke="#f28a1e" stroke-width="3"/></svg>

<article class="abs news" style="top:494px">
  <div class="date">10<small>MAR</small></div>
  <div class="news-body">
    <div class="news-title">DONEC MALESUADA SAPIEN A NEQUE VESTIBULUM</div>
    <div class="news-meta">Lorem Ipsum Dolor</div>
    <div class="news-text">Nunc urna augue, pulvinar non accumsan nec, luctus vel elit. Vivamus nec mi arcu.</div>
    <div class="news-more">read more...</div>
  </div>
</article>
<div class="abs rule" style="top:606px"></div>
<article class="abs news" style="top:626px">
  <div class="date">10<small>MAR</small></div>
  <div class="news-body">
    <div class="news-title">DONEC MALESUADA SAPIEN A NEQUE VESTIBULUM</div>
    <div class="news-meta">Lorem Ipsum Dolor</div>
    <div class="news-text">Nunc urna augue, pulvinar non accumsan nec, luctus vel elit. Vivamus nec mi arcu.</div>
    <div class="news-more">read more...</div>
  </div>
</article>
<div class="abs rule" style="top:738px"></div>

<div class="abs side-bar" style="top:792px">TODAY’S PICKS</div>
<svg class="abs side-icon" style="top:780px;left:652px" viewBox="0 0 36 36" aria-hidden="true"><path d="M18 2L22.5 13H34L25 20L28.5 32L18 25L7.5 32L11 20L2 13H13.5Z" fill="#f6b23a" stroke="#d98a10"/></svg>
<p class="abs picks-intro">Look at what others in your area have<br>been interested in!</p>
<div class="abs thumb" style="left:662px;top:882px;height:44px" role="img" aria-label="Photo of red high heels"><div style="background:linear-gradient(90deg,#fff,#d8262a 50%,#fff)"></div></div>
<div class="abs thumb" style="left:757px;top:882px;height:44px" role="img" aria-label="Photo of a lit hotel tower at night"><div style="background:linear-gradient(#1a1a2a,#3a3a4a 60%,#c08a30)"></div></div>
<div class="abs thumb" style="left:662px;top:932px;height:45px" role="img" aria-label="Photo of a lit hotel tower at night"><div style="background:linear-gradient(#1a1a2a,#3a3a4a 60%,#c08a30)"></div></div>
<div class="abs thumb" style="left:757px;top:932px;height:45px" role="img" aria-label="Photo of a green park with trees"><div style="background:linear-gradient(#3a4a5a,#4a8a3a 50%,#2a5a2a)"></div></div>
<div class="abs thumb" style="left:662px;top:982px;height:46px" role="img" aria-label="Photo of a green park with trees"><div style="background:linear-gradient(#3a4a5a,#4a8a3a 50%,#2a5a2a)"></div></div>
<div class="abs thumb" style="left:757px;top:982px;height:46px" role="img" aria-label="Photo of a drink and dessert"><div style="background:linear-gradient(90deg,#5a1a12,#e09a3a)"></div></div>

<footer class="abs footer"></footer>
<div class="abs foot-mark"></div>
<div class="abs foot-logo">tavernik</div>
<p class="abs copyright">Copyright Tavernik 2011. All Rights Reserved.</p>
<p class="abs foot-links" style="top:1114px">Home<i>I</i>About Us<i>I</i>Catehories<i>I</i>Blog<i>I</i>Contact Us</p>
<p class="abs foot-links" style="top:1136px">Terms of Use<i>I</i>Privacy Policy</p>
</body>
</html>
```